Brimovex business card

Based on company logo and website given , to design a business card temple. Slogan "Your furry friends deserves the best"
Color style please refer to our website

```html
<!DOCTYPE html>
<html lang="en">
<head>
<meta charset="utf-8">
<title>Brimovex business card</title>
<link href="https://fonts.googleapis.com/css2?family=Source+Sans+3:wght@400;600&display=swap" rel="stylesheet">
<style>
  :root {
    --stage: #e6e6e4;
    --card: #ffffff;
    --olive: #b8ad2b;
    --teal: #05474a;
    --leaf: #3b6a55;
    --photo-light: #ecdcc4;
    --photo-dark: #d2ad7c;
    --ink-light: #ffffff;
  }
  * { box-sizing: border-box; margin: 0; padding: 0; }
  html, body {
    width: 1200px; height: 1036px; overflow: hidden;
    background: var(--stage);
    font-family: "Source Sans 3", "Myriad Pro", Arial, sans-serif;
  }
  .card {
    position: absolute; left: 220px; width: 760px; height: 420px;
    background: var(--card); overflow: hidden;
    box-shadow: 0 6px 18px rgba(0,0,0,0.18);
  }
  .card--front { top: 60px; }
  .card--back { top: 556px; }

  .front__name {
    position: absolute; left: 0; right: 0; top: 112px;
    text-align: center; color: var(--olive);
    font-size: 128px; font-weight: 600; line-height: 1; letter-spacing: -1px;
  }
  .front__url {
    position: absolute; left: 210px; top: 262px;
    color: var(--olive); font-size: 28px; font-weight: 400;
  }

  .back__shapes { position: absolute; inset: 0; width: 760px; height: 420px; }
  .back__photo {
    position: absolute; left: 60px; top: 30px; width: 320px; height: 390px;
    background: linear-gradient(160deg, var(--photo-light), var(--photo-dark));
  }
  .back__name {
    position: absolute; left: 390px; top: 50px; width: 340px;
    text-align: center; color: var(--olive);
    font-size: 66px; font-weight: 600; line-height: 1;
  }
  .back__services {
    position: absolute; left: 420px; top: 130px; width: 300px;
    display: flex; justify-content: center; gap: 26px;
    color: var(--leaf); font-size: 16px; font-weight: 400;
  }
  .contact {
    position: absolute; left: 452px; top: 272px;
    list-style: none; color: var(--ink-light);
    font-size: 15.5px; line-height: 19px;
  }
  .contact__item { display: flex; align-items: flex-start; margin-bottom: 2px; }
  .contact__icon { width: 16px; height: 16px; margin: 2px 14px 0 0; flex: none; fill: var(--ink-light); }
</style>
</head>
<body>

<section class="card card--front">
  <div class="front__name">Brimovex</div>
  <div class="front__url">www.brimovex.com.au</div>
</section>

<section class="card card--back">
  <svg class="back__shapes" viewBox="0 0 760 420" aria-hidden="true">
    <path fill="var(--teal)" d="M0 420 L0 250 C30 185 120 170 240 176 C360 184 450 268 590 258 C670 252 730 222 760 206 L760 420 Z"/>
    <path fill="var(--olive)" d="M320 140 C400 190 480 222 560 224 C640 226 700 205 745 172 C705 212 640 238 560 238 C470 238 390 200 320 140 Z"/>
  </svg>
  <div class="back__photo" role="img" aria-label="Photo of a golden retriever puppy"></div>

  <div class="back__name">Brimovex</div>
  <div class="back__services"><span>Pet Diets</span><span>Vet Medicine</span><span>Service</span></div>

  <ul class="contact">
    <li class="contact__item">
      <svg class="contact__icon" viewBox="0 0 16 16"><path d="M8 1 L1 7 L3 7 L3 15 L7 15 L7 10 L9 10 L9 15 L13 15 L13 7 L15 7 Z"/></svg>
      <span>12/40 Harlow Street<br>Glen Ashby Vic 3188</span>
    </li>
    <li class="contact__item">
      <svg class="contact__icon" viewBox="0 0 16 16"><path d="M3 1 L6 1 L7 5 L5 6.5 C6 9 7.5 10.5 9.5 11 L11 9 L15 10 L15 13 C15 14 14 15 13 15 C7 15 1 9 1 3 C1 2 2 1 3 1 Z"/></svg>
      <span>+61 3 9000 4821<br>1800 000 417</span>
    </li>
    <li class="contact__item">
      <svg class="contact__icon" viewBox="0 0 16 16"><circle cx="8" cy="8" r="7"/><path fill="var(--teal)" d="M4 4 C6 4 7 6 6 7 C5 8 6 10 4 11 C3 9 3 6 4 4 Z M9 3 C11 4 12 5 12 7 C10 7 9 6 9 3 Z M9 10 C11 10 12 11 11 13 C10 13 9 12 9 10 Z"/></svg>
      <span>www.brimovex.com.au</span>
    </li>
    <li class="contact__item">
      <svg class="contact__icon" viewBox="0 0 16 16"><path d="M1 4 L15 4 L15 13 L1 13 Z"/><path d="M1 4 L8 9.5 L15 4" fill="none" stroke="var(--teal)" stroke-width="1.3"/></svg>
      <span>sales@brimovex.com.au</span>
    </li>
  </ul>
</section>

</body>
</html>
```